Professional Business Cards

We need a nice looking, profession and modern business card for our new company. Our logo is attatched

Target Market(s)

Young Professionals

Industry/Entity Type

Financial

Contact Information for Business Card

FRONT

Morvane Tally Pty Ltd
Level 22, Halden Court, 48 Wirrapool St
Sydney NSW 2000
ABN : 57 304 918 226

Derek Wallis - Chief Operations Officer
P : 02 7153 2819
M: 0418 395 207
derek@morvanetally,com

BACK

- Cryptocurrency Exchange Services
- Cryptocurrency Mining Operations
- Cryptocurrency Investment Fund Offering

Font styles to use
Sans Serif

Colors
0255a3
9d9d9d

```html
<!DOCTYPE html>
<html lang="en">
<head>
<meta charset="utf-8">
<title>Morvane Tally Business Card</title>
<link rel="stylesheet" href="https://fonts.googleapis.com/css2?family=Montserrat:wght@400;500;600;700&display=swap">
<style>
  :root {
    --brand-blue: #0255a3;
    --brand-blue-light: #0a62b3;
    --brand-grey: #9d9d9d;
    --text-grey: #555a60;
    --card-white: #ffffff;
    --backdrop: #e9eaec;
  }
  * { box-sizing: border-box; margin: 0; padding: 0; }
  html, body {
    width: 1200px; height: 900px; overflow: hidden;
    background: var(--backdrop);
    font-family: "Montserrat", sans-serif;
  }
  .stage { position: relative; width: 1200px; height: 900px; }
  .card {
    position: absolute; width: 620px; height: 354px;
    box-shadow: 0 8px 24px rgba(0,0,0,0.18);
    overflow: hidden;
  }
  /* Front */
  .card-front { left: 490px; top: 70px; background: var(--card-white); }
  .front-band { position: absolute; left: 0; top: 0; width: 170px; height: 354px; }
  .brand {
    position: absolute; left: 42px; top: 38px;
    display: flex; align-items: center; gap: 12px;
  }
  .brand-square { width: 34px; height: 34px; background: var(--brand-grey); }
  .brand-name {
    font-weight: 700; font-size: 30px; letter-spacing: 1px;
    color: var(--card-white); white-space: nowrap;
  }
  .brand-name-wrap {
    background: var(--card-white); padding: 4px 10px;
  }
  .brand-name-wrap .brand-name { color: var(--brand-blue); }
  .person {
    position: absolute; right: 34px; top: 96px; text-align: right;
  }
  .person-name { font-weight: 700; font-size: 20px; color: var(--brand-blue); }
  .person-title { font-size: 14px; color: var(--text-grey); margin-top: 2px; }
  .contact-list { list-style: none; margin-top: 14px; }
  .contact-list li {
    display: flex; justify-content: flex-end; align-items: center; gap: 6px;
    font-size: 14px; color: var(--text-grey); line-height: 20px;
  }
  .contact-list svg { width: 11px; height: 11px; fill: var(--brand-blue); flex: none; }
  .company {
    position: absolute; right: 34px; bottom: 26px; text-align: right;
    font-size: 14px; color: var(--text-grey); line-height: 20px;
  }
  .company-name { font-weight: 600; color: var(--brand-blue); }
  /* Back */
  .card-back {
    left: 100px; top: 470px;
    background: linear-gradient(135deg, var(--brand-blue) 0%, var(--brand-blue-light) 100%);
    color: var(--card-white);
  }
  .services { list-style: none; position: absolute; left: 34px; top: 30px; }
  .services li {
    font-size: 14px; line-height: 24px; display: flex; align-items: center; gap: 8px;
  }
  .services li::before {
    content: ""; width: 6px; height: 6px; background: var(--card-white);
    transform: rotate(45deg); flex: none;
  }
  .back-web { position: absolute; left: 34px; bottom: 28px; font-size: 13px; font-weight: 500; }
</style>
</head>
<body>
<main class="stage">
  <section class="card card-front" aria-label="Business card front">
    <svg class="front-band" viewBox="0 0 170 354" aria-hidden="true">
      <polygon points="0,0 170,0 90,354 0,354" fill="var(--brand-blue)"/>
    </svg>
    <div class="brand">
      <span class="brand-square"></span>
      <span class="brand-name-wrap"><span class="brand-name">MORVANE TALLY</span></span>
    </div>
    <div class="person">
      <p class="person-name">Derek Wallis</p>
      <p class="person-title">Chief Operations Officer</p>
      <ul class="contact-list">
        <li>02 7153 2819 <svg viewBox="0 0 24 24"><path d="M6.6 10.8a15 15 0 0 0 6.6 6.6l2.2-2.2a1 1 0 0 1 1-.25 11.4 11.4 0 0 0 3.6.57 1 1 0 0 1 1 1V20a1 1 0 0 1-1 1A17 17 0 0 1 3 4a1 1 0 0 1 1-1h3.5a1 1 0 0 1 1 1c0 1.25.2 2.45.57 3.57a1 1 0 0 1-.25 1z"/></svg></li>
        <li>0418 395 207 <svg viewBox="0 0 24 24"><path d="M7 1h10a2 2 0 0 1 2 2v18a2 2 0 0 1-2 2H7a2 2 0 0 1-2-2V3a2 2 0 0 1 2-2zm0 3v14h10V4z"/></svg></li>
        <li>derek@morvanetally,com <svg viewBox="0 0 24 24"><path d="M2 5h20v14H2zm2 2v.5l8 5 8-5V7z"/></svg></li>
        <li>www.morvanetally,com <svg viewBox="0 0 24 24"><path d="M12 2a10 10 0 1 0 0 20 10 10 0 0 0 0-20zm6.9 9h-3a15 15 0 0 0-1.3-6 8 8 0 0 1 4.3 6zM12 4c.9 1.2 1.7 3.8 1.9 7h-3.8C10.3 7.8 11.1 5.2 12 4zM9.4 5a15 15 0 0 0-1.3 6h-3a8 8 0 0 1 4.3-6zM5.1 13h3a15 15 0 0 0 1.3 6 8 8 0 0 1-4.3-6zm5 0h3.8c-.2 3.2-1 5.8-1.9 7-.9-1.2-1.7-3.8-1.9-7zm4.5 6a15 15 0 0 0 1.3-6h3a8 8 0 0 1-4.3 6z"/></svg></li>
      </ul>
    </div>
    <address class="company" style="font-style:normal">
      <p class="company-name">Morvane Tally Pty Ltd</p>
      <p>Level 22, Halden Court, 48 Wirrapool St</p>
      <p>Sydney NSW 2000</p>
      <p>ABN : 57 304 918 226</p>
    </address>
  </section>

  <section class="card card-back" aria-label="Business card back">
    <ul class="services">
      <li>Cryptocurrency Exchange Services</li>
      <li>Cryptocurrency Mining Operations</li>
      <li>Cryptocurrency Investment Fund Offering</li>
    </ul>
    <p class="back-web">www.morvanetally.com</p>
  </section>
</main>
</body>
</html>
```